Criação de Adesivaçao de Veículos para Segurança & Vigilância
A empresa queria:
" Atuamos com portaria remota, onde fazemos toda a automação do controle de acesso de condomínios com equipamentos de última tecnologia e a partir de central de operações remota executamos o atendimento da portaria, com áudio, vídeo e gerenciamento de portas e portões. "

```html
<!DOCTYPE html>
<html lang="pt-BR">
<head>
<meta charset="utf-8">
<title>Adesivação de Veículo – Fortis Segurança</title>
<link rel="stylesheet" href="https://fonts.googleapis.com/css2?family=Montserrat:wght@700;800&display=swap">
<style>
  :root {
    --bg: #f2f2f2;
    --red: #d9141e;
    --black: #1b1b1c;
    --yellow: #f6c312;
    --white: #ffffff;
  }
  html, body {
    margin: 0;
    width: 1200px;
    height: 1200px;
    overflow: hidden;
    background: var(--bg);
    font-family: "Montserrat", Arial, sans-serif;
  }
  .wrap-panel {
    position: absolute;
    left: 100px;
    top: 380px;
    width: 1000px;
    height: 440px;
    border-radius: 28px;
    overflow: hidden;
  }
  .wrap-panel svg {
    position: absolute;
    inset: 0;
    width: 100%;
    height: 100%;
  }
  .brand {
    position: absolute;
    left: 40px;
    top: 128px;
    display: flex;
    align-items: center;
    gap: 12px;
  }
  .brand-mark {
    width: 22px;
    height: 22px;
    background: var(--yellow);
  }
  .brand-name {
    color: var(--white);
    font-weight: 800;
    font-size: 38px;
    letter-spacing: 1px;
  }
  .services {
    position: absolute;
    left: 360px;
    top: 46px;
    margin: 0;
    padding: 0;
    list-style: none;
    color: var(--white);
    font-weight: 700;
    font-size: 13px;
    line-height: 17px;
    letter-spacing: 0.3px;
    text-align: right;
  }
  .phone {
    position: absolute;
    left: 40px;
    top: 300px;
    color: var(--white);
    font-weight: 800;
    font-size: 24px;
    letter-spacing: 1px;
  }
  .slogan {
    position: absolute;
    left: 600px;
    top: 190px;
    color: var(--yellow);
    font-weight: 800;
    font-size: 30px;
    line-height: 36px;
    text-align: center;
  }
</style>
</head>
<body>
  <section class="wrap-panel">
    <svg viewBox="0 0 1000 440" preserveAspectRatio="none" aria-hidden="true">
      <rect class="base-red" x="0" y="0" width="1000" height="440" fill="var(--red)"/>
      <path class="body-black" d="M320 0 C270 110 280 250 400 310 C540 370 720 350 1000 300 L1000 0 Z" fill="var(--black)"/>
      <path class="stripe-yellow" d="M320 0 C270 110 280 250 400 310 C540 370 720 350 1000 300" fill="none" stroke="var(--yellow)" stroke-width="16"/>
      <path class="stripe-white" d="M306 0 C256 115 266 262 392 324 C538 388 720 368 1000 318" fill="none" stroke="var(--white)" stroke-width="7"/>
      <path class="corner-yellow" d="M900 0 L1000 0 L1000 140 C960 90 930 40 900 0 Z" fill="var(--yellow)"/>
    </svg>

    <div class="brand">
      <span class="brand-mark"></span>
      <span class="brand-name">FORTIS</span>
    </div>

    <ul class="services">
      <li>MONITORAMENTO DE ALARME</li>
      <li>MONITORAMENTO DE IMAGENS</li>
      <li>VIGILÂNCIA ARMADA E PORTARIA</li>
      <li>PORTARIA VIRTUAL</li>
      <li>RONDAS ONLINE</li>
      <li>RASTREAMENTO VEICULAR</li>
    </ul>

    <div class="phone">(41) 3000 - 4567</div>

    <div class="slogan">PROTEJA SEU<br>PATRIMÔNIO</div>
  </section>
</body>
</html>
```